Mergers and Acquisitions Business Seeks Fresh Website Design

IMPORTANT: Please only design the Homepage, for the contest. If you win the contest, you will design the inner pages, as see in the attached document 'Travik 2025 website wireframes."
Design a new website for Travik at travik.global. Maintaining current Impact and Open Sans fonts, or using open-source alternatives from Google Fonts.
Enhance the design with a premium feel, impactful visuals, and dynamic content. We want the new design to focus on generating high-quality inquiries, strong calls to action, and consistent branding.
Industry/Entity Type
Mergers and Acquisitions
Number of Pages Required
5+ page
Font styles to use
Other font styles liked:
- See Website Brief file
Requirements
Must have
- Consistency in layout, colours, fonts and overall design
Should not have
- Very bright colours, hard to read fonts, unlicensed images and fonts

```html
<!DOCTYPE html>
<html lang="en">
<head>
<meta charset="utf-8">
<title>Travik – Ideal Origination</title>
<link rel="stylesheet" href="https://fonts.googleapis.com/css2?family=Anton&family=Bebas+Neue&family=Poppins:wght@400;500;600&display=swap">
<style>
:root{
  --purple:#54205e;
  --purple-soft:#ddd2e1;
  --ink:#5f5f5f;
  --text:#555;
  --line:#d8d8d8;
  --bg:#dcdcdc;
  --white:#fff;
  --display:"Anton",Impact,sans-serif;
  --head:"Bebas Neue",Impact,sans-serif;
  --body:"Poppins","Open Sans",sans-serif;
}
*{box-sizing:border-box;margin:0;padding:0}
html,body{width:1187px;height:1200px;overflow:hidden}
body{background:var(--bg);position:relative;font-family:var(--body);color:var(--text)}
.abs{position:absolute}
.photo{background:linear-gradient(120deg,#9fb6c8 0%,#56738f 45%,#2d4560 100%)}
.photo.meeting{background:linear-gradient(100deg,#7f9bb3 0%,#4c6a86 40%,#8c7866 62%,#c9d6e0 100%)}
.photo.warm{background:linear-gradient(135deg,#d6c1a6 0%,#9b7b5e 50%,#4e3d32 100%)}
.photo.light{background:linear-gradient(135deg,#eef2f4 0%,#b9c6cf 55%,#7f8f99 100%)}
.photo.dark{background:linear-gradient(120deg,#51627c 0%,#23344d 45%,#0e1828 100%)}
.photo.tech{background:linear-gradient(135deg,#2f4a66 0%,#1b2b40 60%,#0f1a29 100%)}

/* ---------- desktop hero view ---------- */
.desktop{left:120px;top:394px;width:653px;height:419px;background:var(--white);overflow:hidden;transform:scale(.621);transform-origin:0 0}
.desktop .logo{left:42px;top:4px;font-family:var(--display);font-size:64px;color:var(--purple);line-height:80px}
.btn-outline{border:1px solid var(--purple);color:var(--purple);font-family:var(--head);display:flex;align-items:center;justify-content:center;gap:8px;background:var(--white);white-space:nowrap}
.desktop .contact{left:297px;top:18px;width:155px;height:36px;font-size:23px}
.desktop .phone{left:461px;top:18px;width:155px;height:36px;font-size:23px}
.flag{width:18px;height:12px;background:#1f3a7a;position:relative;display:inline-block;flex:none}
.flag::before{content:"";position:absolute;left:0;right:0;top:4px;height:4px;background:#d22}
.flag::after{content:"";position:absolute;top:0;bottom:0;left:7px;width:4px;background:#d22}
.desktop .rule{left:42px;top:80px;width:573px;height:1px;background:var(--line)}
.desktop .rule-accent{left:42px;top:78px;width:32px;height:2px;background:var(--purple)}
.desktop .nav{left:46px;top:92px;display:flex;gap:11px;font-size:12.5px;color:var(--ink)}
.desktop .rule2{left:42px;top:121px;width:573px;height:1px;background:#eee}
.hero-title{font-family:var(--display);font-weight:400;color:var(--ink);text-transform:uppercase}
.hero-title .accent{color:var(--purple)}
.desktop .hero-title{left:40px;top:128px;font-size:96px;line-height:84px;letter-spacing:-2px}
.desktop .block{left:520px;top:138px;width:96px;height:178px;border-radius:30px;background:var(--purple)}
.desktop .hero-photo{left:42px;top:332px;width:573px;height:100px;border:1px solid var(--purple)}

/* ---------- full homepage view ---------- */
.page{left:797px;top:23px;width:480px;height:2990px;background:var(--white);overflow:hidden;transform:scale(.3854);transform-origin:0 0}
.page .logo{left:31px;top:6px;font-family:var(--display);font-size:44px;color:var(--purple);line-height:56px}
.page .contact{left:216px;top:24px;width:112px;height:23px;font-size:13px}
.page .phone{left:336px;top:24px;width:113px;height:23px;font-size:13px;gap:5px}
.page .phone .flag{width:12px;height:8px}
.page .phone .flag::before{top:3px;height:2px}
.page .phone .flag::after{left:5px;width:2px}
.page .nav{left:33px;top:78px;display:flex;gap:8px;font-size:6px;color:var(--ink)}
.page .hero-title{left:30px;top:106px;font-size:66px;line-height:62px;letter-spacing:-1px}
.page .block{left:380px;top:111px;width:69px;height:129px;border-radius:22px;background:var(--purple)}
.page .hero-photo{left:31px;top:253px;width:418px;height:207px}
.band{left:31px;top:460px;width:418px;height:135px;background:var(--purple);color:var(--white)}
.band h3{position:absolute;left:21px;top:27px;width:80px;font-family:var(--head);font-weight:400;font-size:14px;line-height:14px}
.band p{position:absolute;left:113px;top:22px;width:290px;font-size:6px;line-height:9px}
.faint-block{left:39px;top:620px;width:69px;height:129px;border-radius:22px;background:var(--purple-soft)}
.empower{left:144px;top:620px;width:305px}
.empower h3{font-family:var(--head);font-weight:400;font-size:14.5px;line-height:14px;color:var(--purple);margin-bottom:12px}
.empower li{list-style:none;font-size:5.6px;line-height:13px;display:flex;align-items:center;gap:6px}
.tick{width:7px;height:7px;border-radius:50%;background:var(--purple);flex:none}
.video{left:23px;top:776px;width:431px;height:193px}
.video .caption{position:absolute;left:23px;top:18px;font-size:9.5px;line-height:12px;color:var(--white)}
.video .time{position:absolute;right:18px;top:18px;font-size:9px;color:var(--white);font-weight:600}
.video .play{position:absolute;left:14px;top:145px;width:33px;height:33px;border-radius:50%;background:var(--white)}
.video .play::after{content:"";position:absolute;left:13px;top:10px;border-left:10px solid #111;border-top:6px solid transparent;border-bottom:6px solid transparent}
.video .progress{position:absolute;left:78px;right:18px;top:161px;height:1px;background:rgba(255,255,255,.4)}
.section-title{left:0;width:480px;text-align:center;font-family:var(--head);font-weight:400;font-size:29px;color:var(--purple);line-height:1}
.card{border:1px solid var(--line);background:var(--white);text-align:center;padding-top:13px}
.card h4{font-family:var(--head);font-weight:400;font-size:13px;color:var(--purple)}
.card p{font-size:5.5px;line-height:8px;margin-top:6px;padding:0 25px}
.card.faded{opacity:.3}
.chev{font-size:8px;color:#999}
.subtext{left:120px;width:240px;text-align:center;font-size:5.8px;line-height:9px}
.tile{width:205px;height:134px}
.tile .tile-btn{position:absolute;left:50%;top:80px;transform:translateX(-50%);border:1px solid var(--white);color:var(--white);font-family:var(--head);font-size:12.5px;padding:3px 10px;display:flex;gap:5px;align-items:center;white-space:nowrap}
.stat{left:197px;top:1462px;width:86px;height:86px;border-radius:50%;border:1px solid #999;display:flex;align-items:center;justify-content:center;font-family:var(--head);font-size:30px;color:var(--purple)}
.case-text{text-align:center;width:240px;height:179px;display:flex;flex-direction:column;justify-content:center;align-items:center}
.case-text h4{font-size:9px;font-weight:500;color:var(--purple);line-height:14px}
.case-text p{font-size:5.6px;line-height:8px;margin-top:8px;width:120px}
.case-text .arrow{margin-top:10px;width:12px;height:12px;border:1px solid #bbb;font-size:7px;line-height:10px;color:#999}
.more-line{top:2072px;height:1px;background:#aaa}
.more{left:187px;top:2060px;width:106px;height:25px;font-size:13px}
.insights{left:0;top:2127px;width:480px;height:164px;background:var(--purple)}
.insights h2{position:absolute;left:0;width:480px;top:14px;text-align:center;font-family:var(--head);font-weight:400;font-size:29px;color:var(--white)}
.insight-img{top:2203px;width:97px;height:87px}
.insight-cap{top:2295px;width:97px;text-align:center;font-size:5.4px;line-height:8px;color:#777}
.dots{left:0;width:480px;top:2339px;display:flex;justify-content:center;gap:6px}
.dots span{width:4px;height:4px;border-radius:50%;border:1px solid #888}
.dots span:first-child{background:var(--purple);border-color:var(--purple)}
.map{left:42px;top:2436px;width:395px;height:225px;background:linear-gradient(180deg,#f3f5f6 0%,#d5dbe0 40%,#d5dbe0 70%,#f3f5f6 100%)}
.office h4{font-family:var(--head);font-weight:400;font-size:13px;color:var(--purple);border-bottom:1px solid var(--purple);padding-bottom:3px;margin-bottom:6px;width:130px}
.office p{font-size:5.6px;line-height:9px}
.footer-rule{left:31px;top:2803px;width:418px;height:1px;background:#bbb}
.watermark{left:24px;top:2790px;font-family:var(--display);font-size:160px;line-height:1.1;color:#ede8ef}
.fcol h4{font-family:var(--head);font-weight:400;font-size:13px;color:var(--purple);margin-bottom:5px}
.fcol li{list-style:none;font-size:5.6px;line-height:9px}
.fbtn{width:105px;height:23px;font-size:12px;gap:5px}
.legal{top:2963px;font-size:5.6px}
.legal.right{right:31px;display:flex;gap:10px}
</style>
</head>
<body>

<section class="abs desktop" aria-label="Travik homepage, desktop hero">
  <div class="abs logo">travik</div>
  <div class="abs btn-outline contact">Contact Us</div>
  <div class="abs btn-outline phone"><span class="flag"></span>⌄ 01632 960 400</div>
  <div class="abs rule"></div><div class="abs rule-accent"></div>
  <nav class="abs nav"><span>Home</span><span>Clients ⌄</span><span>Services ⌄</span><span>Private Equity</span><span>Case Studies</span><span>Mandates</span><span>Blog</span><span>Contact</span></nav>
  <div class="abs rule2"></div>
  <h1 class="abs hero-title"><span class="accent">I</span>deal<br>Origination</h1>
  <div class="abs block"></div>
  <div class="abs hero-photo photo meeting" role="img" aria-label="Photo of two businessmen in a meeting with a tablet"></div>
</section>

<main class="abs page" aria-label="Travik homepage, full length">
  <div class="abs logo">travik</div>
  <div class="abs btn-outline contact">Contact Us</div>
  <div class="abs btn-outline phone"><span class="flag"></span>⌄ 01632 960 400</div>
  <nav class="abs nav"><span>Home</span><span>Clients ⌄</span><span>Services ⌄</span><span>Private Equity</span><span>Case Studies</span><span>Mandates</span><span>Blog</span><span>Contact</span></nav>
  <h1 class="abs hero-title"><span class="accent">I</span>deal<br>Origination</h1>
  <div class="abs block"></div>
  <div class="abs hero-photo photo meeting" role="img" aria-label="Photo of two businessmen in a meeting with a tablet"></div>
  <div class="abs band">
    <h3>Exclusive deals, reduced risk, stronger leverage</h3>
    <p>We consistently deliver high-quality deals, bypassing the crowded open market. Imagine a pipeline filled with precise targets aligned with your acquisition goals. Our approach minimises execution risk. We bring forward only well-matched prospects, backed by transparent tracking and guidance, so you negotiate on favourable terms. We focus on quality over quantity, building high-trust seller relationships and a sharper competitive edge for your growth.</p>
  </div>

  <div class="abs faint-block"></div>
  <div class="abs empower">
    <h3>Travik empowers acquirers to outpace competitors by consistently delivering high-response, off-market deal flow, without adding headcount or overhead</h3>
    <ul>
      <li><span class="tick"></span>Find the ideal fit – Target businesses that match your exact criteria</li>
      <li><span class="tick"></span>More options – Access businesses that aren't publicly listed</li>
      <li><span class="tick"></span>No noise – Avoid disruption from advisors and brokers</li>
      <li><span class="tick"></span>Higher-quality deals – Engage with owners who prefer a discreet sale</li>
      <li><span class="tick"></span>More control – Move at your own pace, without broker pressure</li>
      <li><span class="tick"></span>Stronger relationships – Direct contact with business owners</li>
    </ul>
  </div>

  <div class="abs video photo dark" role="img" aria-label="Video still of a business handshake">
    <div class="caption">Exclusive Deals<br>Reduced Risk<br>Stronger Leverage</div>
    <div class="time">3:41</div>
    <div class="play"></div>
    <div class="progress"></div>
  </div>

  <h2 class="abs section-title" style="top:1002px">We Work For</h2>
  <div class="abs card faded" style="left:-110px;top:1051px;width:217px;height:67px"><h4 style="text-align:right;padding-right:180px">Equity</h4><p>Expand your pipeline beyond brokers</p></div>
  <span class="abs chev" style="left:117px;top:1080px">‹</span>
  <div class="abs card" style="left:131px;top:1051px;width:217px;height:67px"><h4>Private Equity</h4><p>Expand your pipeline beyond traditional brokers and geographic boundaries</p></div>
  <span class="abs chev" style="left:358px;top:1080px">›</span>
  <div class="abs card faded" style="left:373px;top:1051px;width:217px;height:67px"><h4 style="text-align:left;padding-left:70px">Private</h4><p>Expand your pipeline beyond</p></div>

  <h2 class="abs section-title" style="top:1152px">If you want ideal flow, let's talk</h2>
  <p class="abs subtext" style="top:1188px">There is only so much you can tell from reviewing our website, the best way to explore is to book a short meeting with one of our team.</p>
  <div class="abs tile photo warm" style="left:31px;top:1239px" role="img" aria-label="Photo of hands typing on a laptop"><span class="tile-btn">☎ 01632 960 400</span></div>
  <div class="abs tile photo tech" style="left:244px;top:1239px" role="img" aria-label="Photo of a laptop with email icons"><span class="tile-btn">✉ Contact Travik</span></div>

  <h2 class="abs section-title" style="top:1407px">Travik the Numbers</h2>
  <div class="abs stat">1:5</div>
  <p class="abs subtext" style="top:1568px;left:170px;width:140px">For every 1 target approached, we analyse at least 5 companies</p>

  <h2 class="abs section-title" style="top:1622px">Recent Case Studies</h2>
  <div class="abs case-text" style="left:0;top:1681px"><h4>Fire Safety Focussed<br>Investment Group</h4><p>A bespoke Fire and Security Solutions Business</p><span class="arrow">›</span></div>
  <div class="abs photo light" style="left:240px;top:1681px;width:240px;height:179px" role="img" aria-label="Photo of colleagues celebrating in an office"></div>
  <div class="abs photo warm" style="left:0;top:1860px;width:240px;height:179px;border:1px solid var(--purple)" role="img" aria-label="Photo of two women working at a laptop"></div>
  <div class="abs case-text" style="left:240px;top:1860px"><h4>Leading Labour<br>Recruitment Company</h4><p>An Established Construction &amp; Recruitment Firm</p><span class="arrow">›</span></div>
  <div class="abs more-line" style="left:31px;width:150px"></div>
  <div class="abs more-line" style="left:299px;width:150px"></div>
  <div class="abs btn-outline more">More Case Studies</div>

  <section class="abs insights"><h2>M&amp;A Insights &amp; Latest Trends</h2></section>
  <div class="abs insight-img photo" style="left:31px" role="img" aria-label="Photo of a team meeting"></div>
  <div class="abs insight-img photo warm" style="left:138px" role="img" aria-label="Photo of a desk seen from above"></div>
  <div class="abs insight-img photo light" style="left:245px" role="img" aria-label="Photo of business professionals"></div>
  <div class="abs insight-img photo warm" style="left:352px" role="img" aria-label="Photo of colleagues at a table"></div>
  <p class="abs insight-cap" style="left:31px">Why Off Market is Key for the Motivated Buyer</p>
  <p class="abs insight-cap" style="left:138px">Why Off Market is Key for the Motivated Buyer</p>
  <p class="abs insight-cap" style="left:245px">Why Off Market is Key for the Motivated Buyer</p>
  <p class="abs insight-cap" style="left:352px">Why Off Market is Key for the Motivated Buyer</p>
  <div class="abs dots"><span></span><span></span><span></span><span></span></div>

  <h2 class="abs section-title" style="top:2377px">Regional and Cross-Border Deal Makers</h2>
  <div class="abs map" role="img" aria-label="World map marking office and deal locations"></div>
  <div class="abs office" style="left:118px;top:2683px"><h4>UK &amp; Europe Office</h4><p>Fourth Floor Harrow Court<br>House<br>Winslade<br>WN4 2QT<br>Contact: +44 (0) 1632 960 400</p></div>
  <div class="abs office" style="left:292px;top:2683px"><h4>APAC Office</h4><p>7 Harbour Lane, Marrowvale<br>NSW 2999 Australia<br>Contact: +61 (0) 2 5550 1844</p></div>

  <div class="abs footer-rule"></div>
  <div class="abs watermark">travik</div>
  <div class="abs fcol" style="left:31px;top:2830px"><h4>Clients</h4><ul><li>Private Equity</li><li>Trade Buyers</li><li>Management Buy-In</li><li>Search Funds</li><li>Corporate Finance</li></ul></div>
  <div class="abs fcol" style="left:137px;top:2830px"><h4>Services</h4><ul><li>Deal Origination</li><li>Single Acquisitions</li><li>Buy and Build</li><li>Bolt-On Acquisitions</li><li>Cross Border/International</li></ul></div>
  <div class="abs fcol" style="left:236px;top:2848px"><ul><li>Acquisition Finance</li><li>Negotiation Support</li><li>Due Diligence</li></ul></div>
  <div class="abs fcol" style="left:341px;top:2830px"><h4>Contact</h4><ul><li>+44 (0) 1632 960 400</li></ul></div>
  <div class="abs btn-outline fbtn" style="left:341px;top:2863px">✉ Contact Travik</div>
  <div class="abs btn-outline fbtn" style="left:341px;top:2892px">Book Appointment</div>
  <p class="abs legal" style="left:31px">© Travik Limited. All rights reserved</p>
  <p class="abs legal right"><span>Policies</span><span>Terms of Use</span><span>Privacy Policy</span><span>Contact Us</span></p>
</main>

</body>
</html>
```